Letterhead Design Project

Initially, we would like to review our letterheads.

Something simple which uses our corporate imagery well and is nicely balanced.

Please note that I will be following up this letter-head with some customised quote templates and similarly customisable collateral in the next few weeks.

Target Market(s)

Enterprise business

Industry/Entity Type

Quote

Requirements
Must have
• The Nexora9 logo
See www.nexora9.com.au

Our tagline "Enterprise Hosting, Messaging and Server Virtualisation"

Our website address

Ideally in our colour pallette, but will consider submissions which look fantastic and necessitate other colours.

```html
<!DOCTYPE html>
<html lang="en">
<head>
<meta charset="utf-8">
<title>Nexora9 Letterhead</title>
<link href="https://fonts.googleapis.com/css2?family=Arimo:wght@400;700&display=swap" rel="stylesheet">
<style>
  :root {
    --ink: #000000;
    --paper: #ffffff;
    --brand-red: #c91f27;
    --band-dark: #000000;
    --band-gloss: #3a3a3a;
    --frame: #1a1a1a;
  }
  * { margin: 0; padding: 0; box-sizing: border-box; }
  html, body {
    width: 1200px; height: 1000px; overflow: hidden;
    background: var(--paper);
    font-family: "Arimo", Arial, sans-serif;
    color: var(--ink);
  }
  .canvas { position: relative; width: 1200px; height: 1000px; }
  .letterhead {
    position: absolute; left: 305px; top: 85px;
    width: 596px; height: 843px;
    border: 1px solid var(--frame);
    background: var(--paper);
  }
  .masthead {
    position: absolute; left: 0; top: 0; width: 100%; height: 58px;
    background: linear-gradient(to bottom, var(--band-dark) 0%, var(--band-gloss) 22%, var(--band-dark) 55%, var(--band-dark) 100%);
  }
  .brand-mark {
    position: absolute; left: 35px; top: 16px;
    width: 32px; height: 32px; background: var(--brand-red);
  }
  .brand-name {
    position: absolute; left: 72px; top: 17px;
    font-size: 30px; font-weight: 700; line-height: 30px;
    color: var(--paper); letter-spacing: -0.6px; white-space: nowrap;
  }
  .tagline {
    position: absolute; left: 196px; top: 38px;
    font-size: 10px; line-height: 12px; color: var(--paper); white-space: nowrap;
  }
  .website {
    position: absolute; right: 37px; top: 38px;
    font-size: 10px; line-height: 12px; color: var(--paper); white-space: nowrap;
  }
  .contact-bar {
    position: absolute; left: 32px; top: 743px; width: 529px; height: 16px;
    background: var(--brand-red); color: var(--paper);
    font-size: 10px; font-weight: 700; text-align: center; line-height: 16px;
  }
  .contact-col {
    position: absolute; top: 763px;
    font-size: 8.3px; line-height: 9.7px; white-space: nowrap;
  }
  .contact-col .heading { color: var(--brand-red); font-weight: 700; }
  .col-company { left: 32px; }
  .col-phone { left: 127px; }
  .col-enquiry { left: 319px; top: 762px; }
  .col-address { left: 454px; top: 771px; font-size: 7.9px; }
  .phone-grid { display: grid; grid-template-columns: 22px 71px 24px auto; }
  .emergency { margin-top: 2px; }
</style>
</head>
<body>
<div class="canvas">
  <div class="letterhead">
    <header class="masthead">
      <div class="brand-mark"></div>
      <div class="brand-name">Nexora9</div>
      <div class="tagline">Enterprise Hosting, Messaging and Server Virtualisation</div>
      <div class="website">www.nexora9.com.au</div>
    </header>

    <footer>
      <div class="contact-bar">Nexora9 Contact Information</div>

      <div class="contact-col col-company">
        <div class="heading">Nexora9 Pty. Ltd.</div>
        <div>Suite 4, Level 3</div>
        <div>18 Harlow Parade,</div>
        <div>Kellsbrook, Australia</div>
        <div>VIC - 3999</div>
      </div>

      <div class="contact-col col-phone">
        <div class="heading">Phone</div>
        <div class="phone-grid">
          <span>VIC:</span><span>+61 3 9555 0142</span><span>NSW:</span><span>+61 2 8555 0155</span>
          <span>QLD:</span><span>+61 7 3555 0187</span><span>ACT:</span><span>+61 2 6555 0198</span>
          <span>WA:</span><span>+61 8 6555 0124</span><span>SA:</span><span>+61 8 7555 0172</span>
        </div>
        <div class="heading emergency">Emergency Response :</div>
        <div>+61 3 9555 0142 Select Voice Menu Option 5</div>
      </div>

      <div class="contact-col col-enquiry">
        <div class="heading">Enquiries</div>
        <div>Sales Enquiries</div>
        <div>Billing Enquiries</div>
        <div>Knowledge Base &amp; Trouble Tickets</div>
        <div>Hosting Support Community</div>
      </div>

      <div class="contact-col col-address">
        <div>sales@nexora9.com.au</div>
        <div>accounts@nexora9.com.au</div>
        <div>https://support.nexora9.com.au/</div>
        <div>https://support.nexora9.com.au/</div>
      </div>
    </footer>
  </div>
</div>
</body>
</html>
```